A4 6 page tri-fold brochure for security screen company

Brochure design and layout for a new company based in the UAE called Harbor Panes. We make clear mesh security screen doors and windows that aesthetically blend with the house, like a fly screen, rather than a traditional heavy looking security screen. We want to project an image of safety and security but with warmth and humanity to it, not just something clinical. Copy hasn't been written yet so use dummy text or pull and adjust copy form our website www.harborpanes-example.ae.
Target market: home owners, financially comfortable, possibly with young children or pets.
Purpose of brochure: to have potential clients contact us (via phone, whatsapp, email or through our website) to arrange a free measure and quote.
More details provided in attached word doc brief and product images, logos etc, attached also.
Please see attached brief.

Target Market(s)

Home owners, financially comfortable, possibly with young children or pets.

Industry/Entity Type

Home Improvement

Font styles to use
Serif
Sans Serif

Colors
0255a3
3176b5
85acd3
cfdfed
eaf1f7

Requirements
Must have
• Good clear images with detailed close ups (or call outs) of specific details such as the mesh and locks.
• Contact details to include website www.harborpanes-example.ae, phone number: +971 50 318 2097, email address: oliver@harborpanes-example.ae
Nice to have
• If your are comfortable using and adjusting the appropriate copy from our website please do so.
• Images - I've included a lot of images so please choose the most appropriate to help sell the product. Some of the better images I like are: _DSC2929, French_Windows, HARBOR_PANES-3204, HARBOR_PANES-3231, HARBOR_PANES-3345, HARBOR_PANES-3354, HARBOR_PANES-3401, Girls room windows1, Girls room windows2, IMG_2968. Please don't limit yourself to these images and use the ones you feel best fit.
Should not have
• Please see attached brief.

```html
<!DOCTYPE html>
<html lang="en">
<head>
<meta charset="utf-8">
<title>Harbor Panes – Tri-fold Brochure</title>
<link rel="stylesheet" href="https://fonts.googleapis.com/css2?family=Michroma&family=Lato:wght@400;700&display=swap">
<style>
  :root{
    --blue:#0a6fc9;
    --navy:#0b3f8f;
    --sky:#85acd3;
    --grey:#8e8f91;
    --grey-dark:#6e7074;
    --ink:#3b3d40;
    --paper:#ffffff;
    --panel-tint:#f3f4f6;
    --stage:#a7a8aa;
    --gold:#d9a233;
  }
  html,body{margin:0;padding:0;width:1200px;height:1200px;overflow:hidden;background:var(--stage);}
  .spread{position:absolute;left:74px;width:1052px;height:490px;background:var(--paper);overflow:hidden;}
  .spread--outside{top:65px;}
  .spread--inside{top:623px;}
  .spread svg{position:absolute;left:0;top:0;}
  .txt{position:absolute;margin:0;}
  .heading{font-family:"Michroma",sans-serif;color:var(--navy);font-size:8.6px;letter-spacing:.2px;white-space:nowrap;}
  .heading--rule{border-bottom:1.5px solid var(--blue);padding-bottom:3px;}
  .subhead{font-family:"Michroma",sans-serif;color:var(--blue);font-size:7.4px;white-space:nowrap;}
  .body{font-family:"Lato",sans-serif;color:var(--ink);font-size:5.3px;line-height:1.5;}
  .body p{margin:0 0 3px;}
  .cover-title{font-family:"Michroma",sans-serif;color:#fff;font-size:24px;line-height:1.1;white-space:nowrap;}
  .cover-title span{display:inline-block;font-size:19px;border-bottom:2px solid #fff;padding-bottom:4px;margin-top:2px;}
  .warranty-note{font-family:"Lato",sans-serif;font-size:9.3px;color:var(--ink);text-align:center;line-height:1.35;}
  .brand{font-family:"Michroma",sans-serif;display:flex;align-items:center;gap:6px;white-space:nowrap;}
  .brand__mark{width:12px;height:12px;border-radius:50%;background:currentColor;display:inline-block;flex:none;}
  .contact-line{font-family:"Michroma",sans-serif;color:#fff;font-size:13.5px;text-align:center;white-space:nowrap;}
  .contact-line em{font-style:normal;color:var(--blue);border-bottom:1.5px solid var(--blue);}
  .phone{font-family:"Michroma",sans-serif;color:#fff;font-size:22px;text-align:center;white-space:nowrap;}
  .web{font-family:"Lato",sans-serif;color:#fff;font-size:11px;letter-spacing:1.5px;text-align:center;}
  .tagline{font-family:"Michroma",sans-serif;color:var(--grey-dark);font-size:13px;text-align:center;white-space:nowrap;}
  .pill{font-family:"Lato",sans-serif;font-weight:700;color:#fff;background:var(--blue);font-size:17px;text-align:center;border-radius:12px;line-height:24px;}
  .cover-web{font-family:"Lato",sans-serif;font-weight:700;color:var(--navy);font-size:8px;letter-spacing:3px;text-align:center;}
</style>
</head>
<body>

<section class="spread spread--outside">
  <svg width="1052" height="490" viewBox="0 0 1052 490">
    <defs>
      <linearGradient id="photoWarm" x1="0" y1="0" x2="1" y2="1">
        <stop offset="0" stop-color="#d9d2c3"/><stop offset="1" stop-color="#8f8674"/>
      </linearGradient>
      <linearGradient id="photoHouse" x1="0" y1="0" x2="0" y2="1">
        <stop offset="0" stop-color="#cfe0ee"/><stop offset=".35" stop-color="#efe7cf"/><stop offset="1" stop-color="#cbc2a6"/>
      </linearGradient>
      <linearGradient id="greyBlock" x1="0" y1="0" x2="0" y2="1">
        <stop offset="0" stop-color="#9c9d9f"/><stop offset="1" stop-color="#7f8083"/>
      </linearGradient>
      <radialGradient id="sealTone" cx=".5" cy=".5" r=".5">
        <stop offset="0" stop-color="#3a3226"/><stop offset=".7" stop-color="#6f5726"/><stop offset="1" stop-color="#d9a233"/>
      </radialGradient>
    </defs>

    <rect class="panel-tint" x="350" y="0" width="351" height="490" fill="#f2f2f3"/>

    <polygon class="header-band" points="0,0 273,0 273,38 110,80 0,55" fill="var(--blue)"/>
    <polygon class="hex-outline" points="216,35 250,54.5 250,93.5 216,113 182,93.5 182,54.5" fill="none" stroke="var(--navy)" stroke-width="2"/>
    <polygon role="img" aria-label="Photo: shuttered window with mesh screen" points="45,95 120,129 120,197 45,231 -30,197 -30,129" fill="url(#photoWarm)"/>
    <polygon class="hex-outline" points="31,203 54,216 54,242 31,255 8,242 8,216" fill="none" stroke="var(--blue)" stroke-width="2"/>
    <polygon role="img" aria-label="Photo: sliding screen door onto a garden" points="128.5,219 194,256 194,330 128.5,367 63,330 63,256" fill="url(#photoWarm)"/>
    <polygon class="hex-outline" points="166.5,327 190,340 190,366 166.5,379 143,366 143,340" fill="none" stroke="var(--blue)" stroke-width="2"/>
    <polygon role="img" aria-label="Photo: bright room with screened windows" points="45,343 120,385 120,468 45,510 -30,468 -30,385" fill="#d8d6d0"/>
    <polygon class="hex-outline" points="24,467 46,480 46,506 24,519 2,506 2,480" fill="none" stroke="var(--blue)" stroke-width="2"/>

    <polygon class="grey-block" points="350,335 521,195 701,335 701,490 350,490" fill="url(#greyBlock)"/>
    <circle role="img" aria-label="Seal: 10 years warranty" cx="521" cy="122" r="52" fill="url(#sealTone)"/>
    <polygon class="logo-hex" points="525,206 581,238 581,301 525,333 469,301 469,238" fill="var(--blue)"/>
    <polygon class="hex-outline" points="560.5,287 586,301.5 586,330.5 560.5,345 535,330.5 535,301.5" fill="none" stroke="#fff" stroke-width="2"/>
    <circle class="social" cx="483" cy="463" r="10" fill="var(--blue)"/>
    <circle class="social" cx="524" cy="463" r="10" fill="var(--blue)"/>
    <circle class="social" cx="564" cy="463" r="10" fill="var(--blue)"/>

    <polygon role="img" aria-label="Photo: cream two-storey villa with balcony" points="820,0 1052,0 1052,292 760,292 750,40" fill="url(#photoHouse)"/>
    <polyline class="frame-accent" points="814,0 736,31 736,223" fill="none" stroke="var(--blue)" stroke-width="6"/>
    <polygon class="grey-hex" points="986,219 1037,247 1037,303 986,331 935,303 935,247" fill="#7d7e80" opacity=".85"/>
    <polygon class="hex-outline" points="815,168 888,205 888,279 815,314 742,279 742,205" fill="none" stroke="var(--navy)" stroke-width="2.5"/>
    <polygon role="img" aria-label="Close-up: woven stainless steel mesh" points="815,175 881,208 881,274 815,307 749,274 749,208" fill="#1e1f22" stroke="#fff" stroke-width="3"/>
  </svg>

  <h1 class="txt cover-title" style="left:35px;top:12px;">PRODUCT<br><span>DETAILS</span></h1>

  <h3 class="txt subhead" style="left:138px;top:143px;">LOREM IPSUM</h3>
  <div class="txt body" style="left:138px;top:155px;width:188px;">
    <p>Fine stainless mesh keeps air moving while the frame stays locked and secure. Each screen is measured and fitted to your home by our own team.</p>
    <p>Clean lines, quiet finish, lasting strength.</p>
  </div>
  <h3 class="txt subhead" style="left:207px;top:258px;">LOREM IPSUM</h3>
  <div class="txt body" style="left:207px;top:271px;width:128px;">
    <p>Fine stainless mesh keeps air moving while the frame stays locked and secure. Each screen is measured and fitted to your home by our own team.</p>
    <p>Clean lines, quiet finish, lasting strength.</p>
  </div>
  <h3 class="txt subhead" style="left:138px;top:398px;">LOREM IPSUM</h3>
  <div class="txt body" style="left:138px;top:410px;width:188px;">
    <p>Fine stainless mesh keeps air moving while the frame stays locked and secure. Each screen is measured and fitted to your home by our own team.</p>
    <p>Clean lines, quiet finish, lasting strength.</p>
  </div>

  <p class="txt warranty-note" style="left:372px;top:18px;width:306px;">Should you have any problems with your Harbor Panes, we offer a <b>10 year warranty</b> on all stainless steel mesh and aluminium products and <b>1 year on component parts.</b></p>

  <div class="txt brand" style="left:476px;top:263px;color:#fff;font-size:8.5px;gap:5px;"><span class="brand__mark" style="width:8px;height:8px;"></span>HARBOR PANES</div>

  <p class="txt contact-line" style="left:350px;top:368px;width:351px;">CONTACT US FOR A <em>FREE QUOTE:</em></p>
  <p class="txt phone" style="left:350px;top:395px;width:351px;">+971 50 318 2097</p>
  <p class="txt web" style="left:350px;top:428px;width:351px;">www.harborpanes-example.ae</p>

  <div class="txt brand" style="left:701px;top:348px;width:351px;justify-content:center;color:var(--navy);font-size:19px;"><span class="brand__mark" style="color:var(--blue);"></span>HARBOR PANES</div>
  <p class="txt tagline" style="left:701px;top:394px;width:351px;">SERIOUSLY STRONG SCREENS</p>
  <p class="txt pill" style="left:769px;top:415px;width:220px;">that let the breeze in and</p>
  <p class="txt tagline" style="left:701px;top:446px;width:351px;">KEEP INTRUDERS (AND BUGS) OUT!</p>
  <p class="txt cover-web" style="left:701px;top:469px;width:351px;">www.harborpanes-example.ae</p>
</section>

<section class="spread spread--inside">
  <svg width="1052" height="490" viewBox="0 0 1052 490">
    <defs>
      <linearGradient id="photoVilla" x1="0" y1="0" x2="1" y2="1">
        <stop offset="0" stop-color="#efe8cf"/><stop offset=".6" stop-color="#d9d1b5"/><stop offset="1" stop-color="#6d7072"/>
      </linearGradient>
      <linearGradient id="photoRoom" x1="0" y1="0" x2="1" y2="1">
        <stop offset="0" stop-color="#e7e2d8"/><stop offset="1" stop-color="#9d9486"/>
      </linearGradient>
    </defs>
    <rect class="panel-tint" x="701" y="0" width="351" height="490" fill="#f6f6f7"/>

    <polygon role="img" aria-label="Photo: villa terrace with screened sliding doors" points="0,345 170,245 300,218 588,386 588,490 0,490" fill="url(#photoVilla)"/>
    <polygon class="accent-block" points="588,386 678,440 678,490 588,490" fill="var(--blue)"/>
    <polygon role="img" aria-label="Close-up: fine grey security mesh" points="97,205 166,244 166,322 97,361 28,322 28,244" fill="#6f7580"/>
    <polygon class="hex-outline" points="154.5,277 194,299 194,343 154.5,365 115,343 115,299" fill="none" stroke="#fff" stroke-width="2"/>

    <polygon role="img" aria-label="Photo: sliding screen door in a living room" points="419,41 470,72 470,134 419,165 368,134 368,72" fill="url(#photoRoom)"/>
    <polygon class="hex-outline" points="390,117 410,128 410,150 390,161 370,150 370,128" fill="none" stroke="var(--blue)" stroke-width="2"/>
    <polygon role="img" aria-label="Photo: sliding screen door close-up" points="639,161 690,193 690,257 639,289 588,257 588,193" fill="url(#photoRoom)"/>
    <polygon class="hex-outline" points="616,247 634,257.5 634,278.5 616,289 598,278.5 598,257.5" fill="none" stroke="var(--blue)" stroke-width="2"/>

    <polygon role="img" aria-label="Photo: hinged screen door over timber door" points="779,13 842,50 842,124 779,161 716,124 716,50" fill="#8a6a4c"/>
    <polygon class="hex-outline" points="743.5,114 767,128 767,155 743.5,169 720,155 720,128" fill="none" stroke="var(--blue)" stroke-width="2"/>
    <polygon role="img" aria-label="Photo: screened French doors" points="826,161 890,198 890,272 826,309 762,272 762,198" fill="url(#photoRoom)"/>
    <polygon class="hex-outline" points="798.5,265 822,277 822,302 798.5,314 775,302 775,277" fill="none" stroke="var(--blue)" stroke-width="2"/>
    <polygon role="img" aria-label="Photo: screened French windows with garden view" points="778,329 842,367 842,443 778,481 714,443 714,367" fill="#c7d5dc"/>
    <polygon class="hex-outline" points="749,429 772,442 772,468 749,481 726,468 726,442" fill="none" stroke="var(--blue)" stroke-width="2"/>
  </svg>

  <h2 class="txt heading" style="left:18px;top:17px;">GENERAL INFO</h2>
  <div class="txt body" style="left:18px;top:33px;width:316px;">
    <p>Our screens look like a simple fly screen yet hold firm against force. The woven steel mesh stays clear from inside, so views, light and breeze all remain part of the room.</p>
    <p>Our screens look like a simple fly screen yet hold firm against force. The woven steel mesh stays clear from inside, so views, light and breeze all remain part of the room.</p>
  </div>
  <h2 class="txt heading" style="left:18px;top:90px;">PRIMARY BENEFITS</h2>
  <div class="txt body" style="left:18px;top:105px;width:316px;">
    <p>Our screens look like a simple fly screen yet hold firm against force. The woven steel mesh stays clear from inside, so views, light and breeze all remain part of the room.</p>
    <p>Our screens look like a simple fly screen yet hold firm against force. The woven steel mesh stays clear from inside, so views, light and breeze all remain part of the room.</p>
    <p>Our screens look like a simple fly screen yet hold firm against force. The woven steel mesh stays clear from inside, so views, light and breeze all remain part of the room.</p>
  </div>

  <h2 class="txt heading heading--rule" style="left:374px;top:15px;">SLIDING SCREEN DOORS</h2>
  <h3 class="txt subhead" style="left:482px;top:72px;">LOREM IPSUM</h3>
  <div class="txt body" style="left:482px;top:83px;width:186px;">
    <p>Slim aluminium frames and a hidden lock give a clean finish. The mesh resists cuts and pushes while letting fresh air flow through the home.</p>
  </div>
  <h3 class="txt subhead" style="left:366px;top:195px;width:211px;text-align:right;">LOREM IPSUM</h3>
  <div class="txt body" style="left:366px;top:207px;width:211px;">
    <p>Slim aluminium frames and a hidden lock give a clean finish. The mesh resists cuts and pushes while letting fresh air flow through the home.</p>
  </div>

  <h2 class="txt heading heading--rule" style="left:855px;top:54px;">HINGED DOORS</h2>
  <h3 class="txt subhead" style="left:855px;top:74px;">LOREM IPSUM</h3>
  <div class="txt body" style="left:855px;top:85px;width:178px;">
    <p>Slim aluminium frames and a hidden lock give a clean finish. The mesh resists cuts and pushes while letting fresh air flow through the home.</p>
  </div>
  <h2 class="txt heading heading--rule" style="left:907px;top:201px;">FRENCH DOORS</h2>
  <h3 class="txt subhead" style="left:907px;top:221px;">LOREM IPSUM</h3>
  <div class="txt body" style="left:907px;top:232px;width:126px;">
    <p>Slim aluminium frames and a hidden lock give a clean finish. The mesh resists cuts and pushes while letting fresh air flow through the home.</p>
  </div>
  <h2 class="txt heading heading--rule" style="left:860px;top:375px;">FRENCH WINDOWS</h2>
  <h3 class="txt subhead" style="left:860px;top:397px;">LOREM IPSUM</h3>
  <div class="txt body" style="left:860px;top:408px;width:174px;">
    <p>Slim aluminium frames and a hidden lock give a clean finish. The mesh resists cuts and pushes while letting fresh air flow through the home.</p>
  </div>
</section>

</body>
</html>
```